Financial Research Company Brand Ad

We need a poster design for "Varnholt Analytics" 254mm(h) x 190mm (w) Our research focuses on banks, bank credit, liquidity & corporate solvency. Our believes "Get the credit & liquidity trends right & the rest follows" Please see our website for more information. www.varnholt-analytics.example

Industry/Entity Type

Bank

```html
<!DOCTYPE html>
<html lang="en">
<head>
<meta charset="utf-8">
<title>Varnholt Analytics – Research Poster</title>
<link rel="stylesheet" href="https://fonts.googleapis.com/css2?family=Ubuntu:wght@700&family=Roboto+Condensed:wght@400;700&display=swap">
<style>
  :root {
    --sky-deep: #1b8fe0;
    --sky-mid: #5cc0f4;
    --sky-light: #e4f6ff;
    --globe-edge: #2f9be6;
    --band-white: rgba(255, 255, 255, 0.6);
    --ink: #111111;
    --navy: #0e1a73;
    --menu-ink: #13226e;
    --footer-bg: #e4e7e6;
    --footer-ink: #34418a;
    --white: #ffffff;
  }
  * { margin: 0; padding: 0; box-sizing: border-box; }
  html, body { width: 898px; height: 1200px; overflow: hidden; background: var(--white); }
  .poster {
    position: relative;
    width: 898px;
    height: 1200px;
    overflow: hidden;
    font-family: "Roboto Condensed", sans-serif;
  }
  .sky {
    position: absolute;
    inset: 0;
    background:
      radial-gradient(circle at 50% 45%, #bfe9ff 0%, transparent 55%),
      linear-gradient(180deg, #4fb2ef 0%, var(--sky-deep) 50%, #3aa6ea 100%);
  }
  .globe-artwork {
    position: absolute;
    left: 14px;
    top: 30px;
    width: 870px;
    height: 870px;
    border-radius: 50%;
    background:
      radial-gradient(circle at 58% 40%, var(--sky-light) 0%, #b5e4fb 30%, #7ccdf6 55%, #46aef0 78%, var(--globe-edge) 100%);
    box-shadow: 0 0 60px 10px rgba(255, 255, 255, 0.45);
  }
  .brand-band {
    position: absolute;
    left: 0;
    top: 184px;
    width: 898px;
    height: 128px;
    background: var(--band-white);
  }
  .brand-mark {
    position: absolute;
    left: 113px;
    top: 151px;
    width: 190px;
    height: 190px;
    border-radius: 50%;
    background: var(--navy);
  }
  .brand-name {
    position: absolute;
    left: 356px;
    top: 214px;
    font-family: "Ubuntu", sans-serif;
    font-weight: 700;
    font-size: 52px;
    line-height: 62px;
    color: var(--ink);
    white-space: nowrap;
  }
  .dome {
    position: absolute;
    left: 0;
    top: 0;
  }
  .focus-list {
    position: absolute;
    left: 0;
    top: 734px;
    width: 898px;
    list-style: none;
    text-align: center;
  }
  .focus-list li {
    height: 68px;
    line-height: 84px;
    font-size: 26px;
    color: var(--menu-ink);
    background:
      radial-gradient(ellipse 46% 4px at 50% 2px, rgba(110,110,110,0.55), transparent 100%) top / 100% 8px no-repeat;
  }
  .web-band {
    position: absolute;
    left: 0;
    top: 1028px;
    width: 898px;
    height: 84px;
    background: var(--navy);
    color: var(--white);
    text-align: center;
    font-weight: 700;
    font-size: 30px;
    line-height: 84px;
  }
  .contact {
    position: absolute;
    left: 0;
    top: 1112px;
    width: 898px;
    height: 88px;
    background: var(--footer-bg);
    color: var(--footer-ink);
    text-align: center;
    font-size: 20px;
    line-height: 30px;
    padding-top: 15px;
  }
  .contact .sep { padding: 0 14px; }
</style>
</head>
<body>
<main class="poster">
  <div class="sky"></div>
  <div class="globe-artwork" role="img" aria-label="Glowing blue earth globe covered by a network of connecting lines, set against a sparkling starry sky"></div>

  <div class="brand-band"></div>
  <div class="brand-mark"></div>
  <h1 class="brand-name">Varnholt Analytics</h1>

  <svg class="dome" width="898" height="1200" viewBox="0 0 898 1200" aria-hidden="true">
    <defs>
      <linearGradient id="domeFill" x1="0" y1="0" x2="0" y2="1">
        <stop offset="0" stop-color="#ffffff"/>
        <stop offset="1" stop-color="#eceeee"/>
      </linearGradient>
      <radialGradient id="domeShade" cx="0.5" cy="0.5" r="0.5">
        <stop offset="0.85" stop-color="#3d4a66" stop-opacity="0.6"/>
        <stop offset="1" stop-color="#3d4a66" stop-opacity="0"/>
      </radialGradient>
    </defs>
    <circle cx="425" cy="1080" r="510" fill="url(#domeShade)"/>
    <circle cx="449" cy="1098" r="470" fill="url(#domeFill)"/>
  </svg>

  <ul class="focus-list">
    <li>Banks</li>
    <li>Bank Credit</li>
    <li>Liquidity</li>
    <li>Corporate Solvency</li>
  </ul>

  <div class="web-band">www.varnholt-analytics.example</div>

  <footer class="contact">
    <p>Harlow Court 512 18 Linden Street. Midtown, Port Avery</p>
    <p>Tel: +01 5550 0142<span class="sep">|</span>info@varnholt-analytics.example</p>
  </footer>
</main>
</body>
</html>
```